Letterhead Design Project

We need s letterhead design for a Non Governmental Organization called 'VELMORIX'. We are into promoting innovative agricultural practices to support food security, poverty alleviation, agrobusiness and wealth creation under environmentally sound practices. We also focus on advocacy for agriculture as the engine of growth of economies in Sub-Saharan Africa and Nigeria in particular. We love the green colour and orange or yellow. The final design should communicate agriculture as source of economic growth, health, good environment and peace.
Updates

Reason: I am out of office for next week and may not have access to the internet.

Industry/Entity Type

Agriculture

```html
<!DOCTYPE html>
<html lang="en">
<head>
<meta charset="utf-8">
<title>VELMORIX Identity – Card and Letterhead</title>
<link rel="stylesheet" href="https://fonts.googleapis.com/css2?family=Questrial&display=swap">
<style>
  :root {
    --stage: #000000;
    --paper: #ffffff;
    --green-deep: #0b6a34;
    --green-fresh: #7dc142;
    --green-wash: #e4eee3;
    --green-mist: #eef5e8;
    --amber: #f4a21d;
    --amber-soft: #f9dfb4;
  }
  * { margin: 0; padding: 0; box-sizing: border-box; }
  html, body {
    width: 1200px;
    height: 960px;
    overflow: hidden;
    background: var(--stage);
  }
  .canvas {
    position: relative;
    width: 1200px;
    height: 960px;
    background: var(--stage);
    font-family: "Questrial", "Helvetica Neue", Arial, sans-serif;
  }

  /* Brand presentation card */
  .brand-card {
    position: absolute;
    left: 20px;
    top: 289px;
    width: 488px;
    height: 363px;
    background: var(--paper);
  }
  .brand-card__dot {
    position: absolute;
    left: 159px;
    top: 34px;
    width: 170px;
    height: 170px;
    border-radius: 50%;
    background: var(--amber);
    border: 10px solid var(--green-deep);
    box-shadow: 0 0 0 4px var(--paper), 0 0 0 7px var(--green-fresh);
  }
  .brand-card__name {
    position: absolute;
    left: 0;
    right: 0;
    top: 246px;
    text-align: center;
    font-size: 90px;
    font-weight: 400;
    line-height: 1;
    letter-spacing: 1px;
    color: var(--green-deep);
    white-space: nowrap;
  }

  /* Letterhead sheet */
  .letterhead {
    position: absolute;
    left: 527px;
    top: 40px;
    width: 650px;
    height: 879px;
    background: var(--paper);
    overflow: hidden;
  }
  .letterhead__mark {
    position: absolute;
    left: 304px;
    top: 20px;
    width: 42px;
    height: 42px;
    border-radius: 50%;
    background: var(--amber);
    border: 4px solid var(--green-deep);
    box-shadow: 0 0 0 2px var(--paper), 0 0 0 3px var(--green-fresh);
  }
  .letterhead__name {
    position: absolute;
    left: 0;
    right: 0;
    top: 73px;
    text-align: center;
    font-size: 20px;
    line-height: 1;
    color: var(--green-deep);
    white-space: nowrap;
  }
  .letterhead__rule {
    position: absolute;
    left: 9px;
    width: 633px;
  }
  .letterhead__rule--deep { top: 99px; height: 1px; background: var(--green-deep); }
  .letterhead__rule--fresh { top: 100px; height: 1px; background: var(--green-fresh); }

  .letterhead__watermark {
    position: absolute;
    left: 170px;
    top: 283px;
    width: 440px;
    height: 440px;
    border-radius: 50%;
    background: var(--green-wash);
    border: 14px solid var(--green-mist);
  }
  .letterhead__watermark-name {
    position: absolute;
    left: 170px;
    width: 440px;
    top: 472px;
    text-align: center;
    font-size: 62px;
    line-height: 1;
    color: var(--amber-soft);
    white-space: nowrap;
  }

  .letterhead__band {
    position: absolute;
    left: 0;
    width: 100%;
  }
  .letterhead__band--fresh { top: 859px; height: 10px; background: var(--green-fresh); }
  .letterhead__band--deep { top: 869px; height: 10px; background: var(--green-deep); }
</style>
</head>
<body>
  <main class="canvas">
    <section class="brand-card" aria-label="Brand name presentation">
      <span class="brand-card__dot" aria-hidden="true"></span>
      <h1 class="brand-card__name">VELMORIX</h1>
    </section>

    <section class="letterhead" aria-label="Letterhead">
      <header>
        <span class="letterhead__mark" aria-hidden="true"></span>
        <p class="letterhead__name">VELMORIX</p>
        <span class="letterhead__rule letterhead__rule--deep"></span>
        <span class="letterhead__rule letterhead__rule--fresh"></span>
      </header>

      <span class="letterhead__watermark" aria-hidden="true"></span>
      <span class="letterhead__watermark-name" aria-hidden="true">VELMORIX</span>

      <footer>
        <span class="letterhead__band letterhead__band--fresh"></span>
        <span class="letterhead__band letterhead__band--deep"></span>
      </footer>
    </section>
  </main>
</body>
</html>
```